Business Card Design Project

Business Card
We are rebranding with a new logo
Industry/Entity Type
Business
Contact Information for Business Card
Dennis Marlow +61 427581962 dennis@qovo.com.au P.O. Box 872 Kelvindale QLD 4309
Requirements
Must have
- Logo

```html
<!DOCTYPE html>
<html lang="en">
<head>
<meta charset="utf-8">
<title>Qovo International — Business Card</title>
<link rel="stylesheet" href="https://fonts.googleapis.com/css2?family=Ubuntu:wght@400;500;700&display=swap">
<style>
  :root {
    --bg: #ece8e2;
    --card: #ffffff;
    --orange: #f28a1e;
    --blue: #1a8fc4;
    --ink: #3d3d3d;
  }
  * { margin: 0; padding: 0; box-sizing: border-box; }
  html, body { width: 1200px; height: 1200px; overflow: hidden; }
  body {
    background: var(--bg);
    font-family: "Ubuntu", sans-serif;
    position: relative;
  }
  .card {
    position: absolute;
    left: 100px;
    top: 314px;
    width: 1000px;
    height: 572px;
    background: var(--card);
    overflow: hidden;
    box-shadow: 0 10px 30px rgba(0,0,0,0.12);
  }
  .card__bands { position: absolute; inset: 0; }
  .brand {
    position: absolute;
    left: 80px;
    top: 110px;
    display: flex;
    align-items: center;
    gap: 18px;
  }
  .brand__dot {
    width: 46px; height: 46px;
    border-radius: 50%;
    background: var(--blue);
  }
  .brand__name {
    font-weight: 500;
    font-size: 52px;
    color: var(--blue);
    letter-spacing: 1px;
  }
  .name-row {
    position: absolute;
    left: 80px;
    right: 70px;
    top: 228px;
    display: flex;
    align-items: flex-end;
    gap: 22px;
  }
  .name-row__divider {
    flex: 1;
    height: 2px;
    background: var(--orange);
    margin-bottom: 9px;
  }
  .name-row__name {
    flex: none;
    font-weight: 700;
    font-size: 40px;
    line-height: 1.1;
    color: var(--orange);
    letter-spacing: 0.5px;
    text-transform: uppercase;
    white-space: nowrap;
  }
  .address {
    position: absolute;
    right: 70px;
    top: 288px;
    text-align: right;
    font-size: 24px;
    line-height: 1.45;
    color: var(--ink);
  }
  .address__line { display: flex; justify-content: flex-end; align-items: center; gap: 10px; white-space: nowrap; }
  .contacts {
    position: absolute;
    left: 80px;
    top: 300px;
    list-style: none;
  }
  .contacts__item {
    display: flex;
    align-items: center;
    gap: 18px;
    font-size: 30px;
    color: var(--ink);
    height: 52px;
    white-space: nowrap;
  }
  .contacts__icon { width: 38px; height: 30px; flex: none; }
</style>
</head>
<body>
  <article class="card">
    <svg class="card__bands" viewBox="0 0 1000 572" preserveAspectRatio="none" aria-hidden="true">
      <polygon points="0,520 690,438 760,572 0,572" fill="var(--blue)"/>
      <polygon points="735,440 1000,372 1000,572 805,572" fill="var(--orange)"/>
    </svg>

    <div class="brand">
      <span class="brand__dot"></span>
      <span class="brand__name">Qovo International</span>
    </div>

    <div class="name-row">
      <span class="name-row__divider"></span>
      <span class="name-row__name">Dennis Marlow</span>
    </div>

    <div class="address">
      <div class="address__line">
        <span>P.O. Box 872</span>
        <svg width="20" height="26" viewBox="0 0 20 26" aria-hidden="true">
          <path d="M10 0C4.5 0 0 4.3 0 9.6 0 16.8 10 26 10 26s10-9.2 10-16.4C20 4.3 15.5 0 10 0zm0 13.5a4 4 0 1 1 0-8 4 4 0 0 1 0 8z" fill="var(--orange)"/>
        </svg>
      </div>
      <div class="address__line">Kelvindale QLD 4309</div>
    </div>

    <ul class="contacts">
      <li class="contacts__item">
        <svg class="contacts__icon" viewBox="0 0 38 30" aria-hidden="true">
          <path d="M2 9c0-4 8-7 17-7s17 3 17 7v3h-8V8c-3-1-6-1.5-9-1.5S13 7 10 8v4H2z" fill="var(--orange)"/>
          <path d="M9 14h20l4 14H5z" fill="var(--orange)"/>
          <circle cx="19" cy="21" r="4" fill="#fff"/>
        </svg>
        <span>+61 427581962</span>
      </li>
      <li class="contacts__item">
        <svg class="contacts__icon" viewBox="0 0 38 30" aria-hidden="true">
          <rect x="2" y="3" width="34" height="24" fill="var(--orange)"/>
          <path d="M2 3l17 14L36 3M2 27l12-12M36 27L24 15" stroke="#fff" stroke-width="2" fill="none"/>
        </svg>
        <span>dennis@qovo.com.au</span>
      </li>
    </ul>
  </article>
</body>
</html>
```